Wellness Coach/Personal trainer needs wordpress site/blog with ecommerce capable membership area

We need a WordPress design for PlumHarborFit.com. This is a blog about wellness, weight loss, and health related topics. Design logo will be provided to the winner.

A great site with a design that we would like to emulate are http://kq4.example. The design should be simple, clean, unique, fun, and distinctive. Above all, it should be highly readable and easy to navigate.

These are the specific sections/categories of the blog that should be included and incorporated into the design SEE BELOW.

Thanks in advance for your consideration
Updates

Reason: I have extended the deadline to evaluate more designs from other pros

Hello all, Please take a minute to review the requirements for this project and please make sure you are capable of meeting ALL the requirements. As you already know I will be making a decision very shortly on whose design I will be moving forward with, if there are any last minute submissions now is the time. Thank you for your time.

Target Market(s)

90 % women 10 % men my clients are usually professionals who value their appearance, health, longevity and time.

Industry/Entity Type

Personal Trainer

Font styles to use
Serif

Colors
886aae
ffcf3e

Requirements
Must have
• Requirements

- start losing weight today.... 555 902 6148 (first line)
- visuals/images and backgrounds to give the idea of wellness, weight loss, healthy living, etc
- navigation menu - home, who we are, what we do, who we serve, blog, contact, members area

1) slider element at top below navigation menu
2) slider element near bottom of page will have testimonials
3) contact form/inquiry form (one page)
4) will provide wellness logo (to give credibility)
5) color scheme purple, gold and white
6) membership area
7) fb, tw, youtube icons
8) footer area - In the footer, there will be smaller company logo, copyright,
disclaimer, privacy policy, terms n conditions, verse of day, and contact info, Phone: (555) 902-6148
Email: support@...
Address:
9) use dummy content/graphic as they will be replaced by real content (the winner will provide instruction on how to make changes to all text and changing graphics)
9) ecommerce enabled / newsletter signup area

```html
<!DOCTYPE html>
<html lang="en">
<head>
<meta charset="utf-8">
<title>PlumHarborFit – Wellness &amp; Weight Loss</title>
<link rel="stylesheet" href="https://fonts.googleapis.com/css2?family=Roboto:wght@300;400;500;700&family=Roboto+Slab:wght@700&display=swap">
<style>
:root{
  --purple:#662d91;
  --purple-soft:#7a4aa3;
  --ink:#333333;
  --muted:#555555;
  --band:#efeef2;
  --footer:#e3e3e6;
  --line:#cfcfd4;
  --white:#ffffff;
  --gold-1:#f3d58a;
  --gold-2:#c9902f;
  --gold-3:#6b4a1e;
}
*{box-sizing:border-box;margin:0;padding:0}
html,body{width:1200px;height:2452px;overflow:hidden}
body{position:relative;background:var(--white);font-family:'Roboto',Arial,sans-serif;color:var(--ink)}
.abs{position:absolute}

/* header */
.site-header{left:0;top:0;width:1200px;height:118px;background:var(--white)}
.brand{left:152px;top:30px;display:flex;align-items:center;gap:14px}
.brand-mark{width:40px;height:40px;border-radius:50%;background:var(--purple)}
.brand-name{font-family:'Roboto Slab',Georgia,serif;font-weight:700;font-size:25px;color:var(--purple)}
.main-nav{left:448px;top:62px;display:flex;font-size:13.5px;font-weight:500;text-transform:uppercase;color:#222}
.main-nav span{padding:0 13px;border-left:1px solid #cfcfcf;line-height:22px}
.main-nav span:first-child{border-left:0;padding-left:7px}

/* hero */
.hero{left:0;top:118px;width:1200px;height:593px;
  background:radial-gradient(ellipse at 70% 30%,#fbe6b0 0%,var(--gold-1) 25%,var(--gold-2) 60%,var(--gold-3) 100%)}
.hero-arrow{top:243px;width:61px;height:61px;background:rgba(120,110,100,.55);display:flex;align-items:center;justify-content:center}
.hero-arrow.prev{left:124px}
.hero-arrow.next{left:1017px}
.hero-title{left:154px;top:364px;font-size:31px;font-weight:400;color:#1a1a1a}
.hero-title .phone{color:var(--purple-soft)}
.hero-dots{left:579px;top:558px;display:flex;gap:3px}
.hero-dots i{width:12px;height:12px;border-radius:50%;background:#111;border:2px solid #111}
.hero-dots i.on{background:#fff}

/* welcome */
.welcome{left:0;top:711px;width:1200px;height:329px;background:var(--band)}
.welcome-photo{left:154px;top:36px;width:332px;height:250px;
  background:linear-gradient(180deg,#f5d39a 0%,#e3a55a 55%,#8a5a2c 100%);
  box-shadow:0 16px 14px -10px rgba(0,0,0,.35)}
.welcome-text{left:520px;top:48px;width:520px}
.welcome-text h2{font-size:17px;font-weight:700;color:var(--purple);margin-bottom:10px}
.welcome-text p{font-size:12.6px;line-height:20px;color:var(--ink)}
.btn{display:inline-block;background:var(--purple);color:#fff;font-size:11.5px;font-weight:700;text-transform:uppercase}
.welcome-text .btn{margin-top:18px;padding:10px 14px}

/* section titles */
.section-title{left:520px;width:155px;height:44px;border:1.5px solid var(--purple);background:var(--white);
  color:var(--purple);font-size:17.5px;display:flex;align-items:center;justify-content:center;text-transform:uppercase}

/* membership */
.member-grid{left:154px;top:1122px;width:892px;display:grid;grid-template-columns:repeat(4,219px);grid-auto-rows:176px;gap:6px 5px}
.member{position:relative;border:1px solid #ddd}
.member-name{position:absolute;left:0;right:0;bottom:0;height:32px;background:rgba(120,120,120,.6);
  color:#fff;font-size:11.5px;font-weight:500;padding:10px 0 0 15px;text-transform:uppercase}

/* testimonials */
.testimonials{left:0;top:1512px;width:1200px;height:373px;background:var(--band)}
.t-arrows{left:551px;top:79px;display:flex;gap:4px}
.t-arrows span{width:37px;height:37px;background:#cfcfd2;display:flex;align-items:center;justify-content:center}
.quote{top:141px;width:262px}
.quote .mark{font-family:Georgia,serif;font-size:52px;line-height:34px;color:#c8c8cc;height:30px}
.quote p{font-size:12.5px;line-height:22px;color:var(--ink);margin-top:8px;height:110px}
.quote .rule{border-top:1px solid var(--line);margin-top:8px}
.author{display:flex;align-items:center;gap:14px;margin-top:14px}
.avatar{width:36px;height:36px;border-radius:50%;background:linear-gradient(#b9a595,#7b6a5e)}
.author b{display:block;font-size:11px;font-weight:700;text-transform:uppercase;color:#222}
.author small{font-size:11.5px;color:#333}

/* contact */
.contact-info{left:220px;top:2040px;width:280px;text-align:center}
.contact-info p{font-size:12.5px;line-height:23px;color:var(--ink);margin-top:22px}
.contact-divider{left:600px;top:1986px;width:1px;height:303px;background:var(--line)}
.field-label{left:623px;font-size:14px;color:#444}
.field{left:700px;width:346px;height:40px;border:1px solid #bdbdc2;background:#fff}
.field.area{height:105px}
.send{left:976px;top:2258px;width:72px;height:31px;display:flex;align-items:center;justify-content:center;font-size:13px;font-weight:500}

/* footer */
.site-footer{left:0;top:2315px;width:1200px;height:137px;background:var(--footer)}
.footer-brand{left:152px;top:28px;display:flex;align-items:center;gap:12px}
.footer-brand .brand-mark{width:34px;height:34px}
.footer-brand .brand-name{font-size:21px}
.footer-contact{right:152px;top:27px;text-align:right;font-size:11.5px;line-height:22px;color:#222}
.footer-contact b{font-weight:500}
.footer-rule{left:152px;top:86px;width:896px;border-top:1px solid #b7b7bd}
.follow{left:152px;top:102px;display:flex;align-items:center;gap:5px;font-size:11px;font-weight:700;text-transform:uppercase;color:#222}
.follow .social{width:19px;height:19px;background:#8a8a94}
.follow .social:first-of-type{margin-left:6px}
.legal{right:152px;top:106px;font-size:10.5px;color:#222}
</style>
</head>
<body>

<header class="site-header abs">
  <div class="brand abs"><span class="brand-mark"></span><span class="brand-name">PlumHarborFit</span></div>
  <nav class="main-nav abs">
    <span>Home</span><span>Who we are</span><span>What we do</span><span>Who we serve</span><span>Contact</span><span>Blog</span><span>Members</span>
  </nav>
</header>

<section class="hero abs" role="img" aria-label="Silhouette of a woman raising both arms against a golden sunset sky">
  <div class="hero-arrow prev abs"><svg width="20" height="34" viewBox="0 0 20 34"><path d="M17 2 3 17l14 15" fill="none" stroke="#fff" stroke-width="2.5"/></svg></div>
  <div class="hero-arrow next abs"><svg width="20" height="34" viewBox="0 0 20 34"><path d="M3 2l14 15L3 32" fill="none" stroke="#fff" stroke-width="2.5"/></svg></div>
  <h1 class="hero-title abs">Start Losing Weight Today.... <span class="phone">555 902 6148</span></h1>
  <div class="hero-dots abs"><i></i><i class="on"></i><i></i><i></i></div>
</section>

<section class="welcome abs">
  <div class="welcome-photo abs" role="img" aria-label="Woman with outstretched arms on a beach at sunset"></div>
  <div class="welcome-text abs">
    <h2>WELCOME TO OUR SITE</h2>
    <p>Lorem Ipsum is simply dummy text of the printing and typesetting industry. Lorem Ipsum has been the industry's standard dummy text ever since the 1500s, when an unknown printer took a galley of type and scrambled it to make a type specimen book. It has survived not only five centuries, but also the leap into electronic typesetting, remaining essentially unchanged. It was popularised in the 1960s with the release of Letraset sheets containing Lorem Ipsum passages, and more recently with desktop publishing software like Aldus PageMaker including versions of Lorem Ipsum.</p>
    <span class="btn">Read more</span>
  </div>
</section>

<div class="section-title abs" style="top:1061px">Membership</div>
<div class="member-grid abs">
  <div class="member" role="img" aria-label="Portrait of member Richard" style="background:linear-gradient(135deg,#dfe6ee,#6f7f92)"><span class="member-name">Richard</span></div>
  <div class="member" role="img" aria-label="Portrait of member Mark" style="background:linear-gradient(135deg,#eef0f2,#9aa3ad)"><span class="member-name">Mark</span></div>
  <div class="member" role="img" aria-label="Portrait of member Mark" style="background:linear-gradient(135deg,#d8dde6,#5d6b82)"><span class="member-name">Mark</span></div>
  <div class="member" role="img" aria-label="Portrait of member Mark" style="background:linear-gradient(135deg,#eef0f4,#a8aebb)"><span class="member-name">Mark</span></div>
  <div class="member" role="img" aria-label="Portrait of member Richard" style="background:linear-gradient(135deg,#a5c46a,#d9b887)"><span class="member-name">Richard</span></div>
  <div class="member" role="img" aria-label="Portrait of member Mark" style="background:linear-gradient(135deg,#8d8d8d,#2e2e30)"><span class="member-name">Mark</span></div>
  <div class="member" role="img" aria-label="Portrait of member Peter" style="background:linear-gradient(135deg,#d39a3a,#3a2a22)"><span class="member-name">Peter</span></div>
  <div class="member" role="img" aria-label="Portrait of member White" style="background:linear-gradient(135deg,#2e6f7d,#c9a27a)"><span class="member-name">White</span></div>
</div>

<section class="testimonials abs">
  <div class="section-title abs" style="top:20px">Testimonials</div>
  <div class="t-arrows abs">
    <span><svg width="10" height="14" viewBox="0 0 10 14"><path d="M8 1 2 7l6 6" fill="none" stroke="#333" stroke-width="2"/></svg></span>
    <span><svg width="10" height="14" viewBox="0 0 10 14"><path d="M2 1l6 6-6 6" fill="none" stroke="#333" stroke-width="2"/></svg></span>
  </div>
  <div class="quote abs" style="left:152px">
    <div class="mark">&ldquo;</div>
    <p>It was popularised in the 1960s with the release of Letraset sheets containing Lorem Ipsum passages, and more recently with desktop publishing software like Aldus PageMaker including versions of Lorem</p>
    <div class="rule"></div>
    <div class="author"><span class="avatar" role="img" aria-label="Client avatar"></span><div><b>Rhea Fontaine</b><small>Sydney</small></div></div>
  </div>
  <div class="quote abs" style="left:463px">
    <div class="mark">&ldquo;</div>
    <p>There are many variations of passages of Lorem Ipsum available, but the majority have suffered alteration in some form, by injected humour, or randomised words which don't look even slightly believable.</p>
    <div class="rule"></div>
    <div class="author"><span class="avatar" role="img" aria-label="Client avatar"></span><div><b>Rhea Fontaine</b><small>Sydney</small></div></div>
  </div>
  <div class="quote abs" style="left:783px">
    <div class="mark">&ldquo;</div>
    <p>The standard chunk of Lorem Ipsum used since the 1500s is reproduced below for those interested. Sections 1.10.32 and 1.10.33 from "de Finibus Bonorum et Malorum".</p>
    <div class="rule"></div>
    <div class="author"><span class="avatar" role="img" aria-label="Client avatar"></span><div><b>Rhea Fontaine</b><small>Sydney</small></div></div>
  </div>
</section>

<div class="section-title abs" style="top:1908px">Contact us</div>
<div class="contact-info abs">
  <svg width="34" height="46" viewBox="0 0 34 46"><path d="M17 1C8 1 1 8 1 17c0 12 16 28 16 28s16-16 16-28C33 8 26 1 17 1z" fill="#b4b4ba"/><circle cx="17" cy="17" r="7" fill="#fff"/></svg>
  <p>It was popularised in the 1960s with the release of Letraset sheets containing Lorem Ipsum passages.</p>
</div>
<div class="contact-divider abs"></div>
<span class="field-label abs" style="top:2002px">Name</span>
<div class="field abs" style="top:1992px"></div>
<span class="field-label abs" style="top:2054px">E Mail</span>
<div class="field abs" style="top:2044px"></div>
<span class="field-label abs" style="top:2105px">Phone</span>
<div class="field abs" style="top:2095px"></div>
<span class="field-label abs" style="top:2157px">Message</span>
<div class="field area abs" style="top:2146px"></div>
<span class="btn send abs">SEND</span>

<footer class="site-footer abs">
  <div class="footer-brand abs"><span class="brand-mark"></span><span class="brand-name">PlumHarborFit</span></div>
  <div class="footer-contact abs">
    <b>Phone: (555) 902-6148 &nbsp;|&nbsp; support@plumharborfit.example</b><br>
    It was popularised in the 1960s with the release of Letraset sheets containing
  </div>
  <div class="footer-rule abs"></div>
  <div class="follow abs">Follow us on
    <span class="social" role="img" aria-label="Social network link"></span>
    <span class="social" role="img" aria-label="Social network link"></span>
    <span class="social" role="img" aria-label="Video channel link"></span>
  </div>
  <div class="legal abs">Disclaimer &nbsp;|&nbsp; Privacy policy | Terms and conditions &nbsp;Verse of day &nbsp;| &nbsp;Copyrights @ 2014 All Rights Reserved</div>
</footer>

</body>
</html>
```